Brisbane IT support business needs our first business card

Hello we are a Brisbane based Information Technology company providing support and services to small and medium sized businesses. We provide a range of services and solutions.

The business name is Wattlebrook Network Computing Services, or WNCS for short.

I am looking for a business card that looks professional (don't we all want that), but most importantly, it most utilize the colours in the logo attached.

Reason: Launched late, extending so people have enough time to actually submit something.

Target Market(s)

Other business owners seeking our IT services, and also home users.

Industry/Entity Type

Business

Requirements
Must have
• Please only use the blue/orange colours in logo attached

```html
<!DOCTYPE html>
<html lang="en">
<head>
<meta charset="utf-8">
<title>WNCS Business Card</title>
<link href="https://fonts.googleapis.com/css2?family=Open+Sans:wght@400;600;700&display=swap" rel="stylesheet">
<style>
  :root {
    --navy: #1b4a64;
    --orange: #e8792a;
    --card: #ffffff;
    --card-back: #f7f7f6;
    --backdrop: #2b2b2b;
  }
  * { box-sizing: border-box; margin: 0; padding: 0; }
  html, body { width: 1200px; height: 800px; overflow: hidden; }
  body {
    background: var(--backdrop);
    font-family: "Open Sans", Arial, sans-serif;
    position: relative;
  }
  .card {
    position: absolute;
    width: 560px;
    height: 320px;
    border-radius: 3px;
    box-shadow: 0 10px 30px rgba(0,0,0,0.45);
  }
  .card-front { left: 120px; top: 70px; background: var(--card); }
  .card-back { left: 520px; top: 410px; background: var(--card-back); }

  .brand { position: absolute; display: flex; align-items: center; }
  .brand-dot { border-radius: 50%; background: var(--navy); flex: none; }
  .brand-name { color: var(--orange); font-weight: 700; letter-spacing: 2px; line-height: 1; }
  .tagline { position: absolute; color: var(--navy); font-weight: 400; white-space: nowrap; }

  .card-front .brand { left: 70px; top: 80px; gap: 36px; }
  .card-front .brand-dot { width: 130px; height: 130px; }
  .card-front .brand-name { font-size: 72px; }
  .card-front .tagline { left: 70px; top: 232px; font-size: 19px; }

  .card-back .brand { left: 40px; top: 180px; gap: 20px; }
  .card-back .brand-dot { width: 74px; height: 74px; }
  .card-back .brand-name { font-size: 40px; }
  .card-back .tagline { left: 40px; top: 266px; font-size: 13px; }

  .holder { position: absolute; left: 180px; top: 70px; }
  .holder-name { color: var(--orange); font-weight: 700; font-size: 17px; }
  .holder-role { color: var(--navy); font-size: 12px; margin-left: 10px; }

  .contacts { position: absolute; left: 345px; top: 72px; list-style: none; }
  .contacts li { display: flex; align-items: center; gap: 18px; height: 28px; color: var(--orange); font-size: 13px; }
  .contacts svg { width: 12px; height: 12px; fill: var(--navy); flex: none; }
</style>
</head>
<body>
  <section class="card card-front">
    <div class="brand">
      <span class="brand-dot"></span>
      <span class="brand-name">WNCS</span>
    </div>
    <p class="tagline">Wattlebrook Network Computing Services</p>
  </section>

  <section class="card card-back">
    <div class="holder">
      <p class="holder-name">Dana Whitfield</p>
      <p class="holder-role">Manager</p>
    </div>
    <ul class="contacts">
      <li>
        <svg viewBox="0 0 24 24" aria-hidden="true"><path d="M6.6 10.8a15 15 0 0 0 6.6 6.6l2.2-2.2a1 1 0 0 1 1-.25 11.4 11.4 0 0 0 3.6.57 1 1 0 0 1 1 1V20a1 1 0 0 1-1 1A17 17 0 0 1 3 4a1 1 0 0 1 1-1h3.5a1 1 0 0 1 1 1c0 1.25.2 2.45.57 3.57a1 1 0 0 1-.25 1z"/></svg>
        00 987 654 321
      </li>
      <li>
        <svg viewBox="0 0 24 24" aria-hidden="true"><circle cx="12" cy="12" r="10"/></svg>
        www.wattlebrook.net
      </li>
      <li>
        <svg viewBox="0 0 24 24" aria-hidden="true"><path d="M2 5h20v14H2z M2 5l10 8 10-8" /></svg>
        hello@wattlebrook.net
      </li>
    </ul>
    <div class="brand">
      <span class="brand-dot"></span>
      <span class="brand-name">WNCS</span>
    </div>
    <p class="tagline">Wattlebrook Network Computing Services</p>
  </section>
</body>
</html>
```